BRACKENRIDGE BUILDERS B-Card

I currently have a b-card design but will be removing the image (tree) from the logo and have text only.
I want the card to be classy and strong within the building and construction industry.
I will be using Spot UV on the cards as per the attached examples. I will also send through some sketched ideas that I have in mind.
The color blue is similar to the image (No. 6) attached images

Target Market(s)

middle to maturre aged.
Home Owners / Renovators and Builders

Industry/Entity Type

Construction

Contact Information for Business Card

BRACKENRIDGE BUILDERS
Name: Dermot Quaile
Title: Project Manager
Mobile: 0412 537 804
Office: (08) 9173 5842
Address: 17C Pellworth Avenue, Kelvale WA 6071
Email: info@brackenridgebuild.com.au
PO Box: 3817 Kelvale WA 6977

Colors
0592cd
33a6d7
85cae6
1b1b1b

Requirements
Must have
• 1. It must have spot UV on the front of card, maybe back of card too
• 2. I really like the blue on image 6. (or at least a really cool electric blue against the charcoal grey background)
• 3. The font must be slimline and modern. Easy to read
• 4. There must be no black used on the card... Only greys and dark charcoal greys
• 5. Use only the text from the logo "Brackenridge Builders" Not the image of the tree. I am wanting the b-cards to be more masculine.
Nice to have
• 1. I like the design concept on image 6. but happy to see what else you can do with the Spot UV
• 2. Unless you have a really cool idea of the image of the tree (from previous logo) Spot UV somewhere in the design concept thats original and different then I am keen to see what you come up with
• 3. Try changing the color of the logo eg. full white or Blue and white
• 4. Another option is to have the Brackenridge Logo on the front of card with the spot UV in the background of text which we specialise in eg, Roofing, Ceiling, Insulation, Gutter Guards, Electrical, Insurance etc and we can add or reduce items as required. Similar to image 12.
Should not have
• Do not include the image of the tree from previous logo. unless you have a really cool idea of Spot UV somewhere in the design concept thats original and different.

```html
<!DOCTYPE html>
<html lang="en">
<head>
<meta charset="utf-8">
<title>Brackenridge Builders – Business Card</title>
<link rel="stylesheet" href="https://fonts.googleapis.com/css2?family=Source+Sans+3:wght@400;600&display=swap">
<style>
  :root {
    --backdrop: #e4e4e2;
    --silver-light: #ffffff;
    --silver-mid: #e6e6e6;
    --silver-dark: #cfcfcf;
    --ink: #1b1b1b;
    --charcoal: #1b1b1b;
    --charcoal-deep: #141414;
    --electric-blue: #33a6d7;
    --tree-silver: rgba(255,255,255,0.45);
    --tree-charcoal: rgba(60,60,60,0.35);
  }
  * { box-sizing: border-box; margin: 0; padding: 0; }
  html, body {
    width: 1200px; height: 900px; overflow: hidden;
    background: var(--backdrop);
    font-family: "Source Sans 3", "Helvetica Neue", Arial, sans-serif;
  }
  .canvas { position: relative; width: 1200px; height: 900px; }

  .card {
    position: absolute;
    border-radius: 16px;
    overflow: hidden;
    box-shadow: 0 10px 30px rgba(0,0,0,0.18);
  }

  /* Contact side */
  .card--front {
    left: 78px; top: 35px; width: 587px; height: 363px;
    background: linear-gradient(135deg, var(--silver-dark) 0%, var(--silver-mid) 45%, var(--silver-light) 100%);
    color: var(--ink);
  }
  .card--front .tree-area {
    position: absolute; left: 0; top: 0; width: 350px; height: 363px;
    background: radial-gradient(ellipse at 45% 40%, var(--tree-silver) 0%, rgba(255,255,255,0.15) 55%, rgba(255,255,255,0) 80%);
  }
  .person-name {
    position: absolute; left: 90px; top: 94px; width: 405px; text-align: center;
    font-size: 23px; font-weight: 600; letter-spacing: 0.5px;
  }
  .person-role {
    position: absolute; left: 90px; top: 125px; width: 405px; text-align: center;
    font-size: 16.5px; font-weight: 400; letter-spacing: 0.4px;
  }
  .divider {
    position: absolute; left: 212px; top: 157px; width: 157px; height: 1.5px;
    background: var(--ink);
  }
  .phones {
    position: absolute; left: 90px; top: 174px; width: 405px; text-align: center;
    font-size: 16.5px; line-height: 25px; letter-spacing: 0.5px;
  }
  .address {
    position: absolute; left: 60px; top: 246px; width: 465px; text-align: center;
    font-size: 16.5px; line-height: 24px; letter-spacing: 0.4px;
  }

  /* Brand side */
  .card--back {
    left: 390px; top: 505px; width: 565px; height: 352px;
    background: var(--charcoal);
  }
  .card--back .tree-area {
    position: absolute; inset: 0;
    background:
      radial-gradient(ellipse at 18% 35%, var(--tree-charcoal) 0%, rgba(60,60,60,0) 45%),
      radial-gradient(ellipse at 88% 55%, var(--tree-charcoal) 0%, rgba(60,60,60,0) 40%),
      linear-gradient(180deg, var(--charcoal) 0%, var(--charcoal-deep) 100%);
  }
  .brand {
    position: absolute; left: 0; top: 141px; width: 565px; text-align: center;
    color: var(--electric-blue); font-weight: 400;
  }
  .brand-name {
    display: block; font-size: 42px; line-height: 44px; letter-spacing: 0.5px;
  }
  .brand-trade {
    display: block; font-size: 19px; letter-spacing: 7px; margin-top: 8px; padding-left: 7px;
  }
</style>
</head>
<body>
<main class="canvas">
  <section class="card card--front" aria-label="Business card contact side">
    <div class="tree-area" role="img" aria-label="Faint spot UV tree illustration"></div>
    <p class="person-name">Dermot Quaile</p>
    <p class="person-role">Project Manager</p>
    <div class="divider"></div>
    <p class="phones">0412 537 804<br>(08) 9173 5842</p>
    <p class="address">17C Pellworth Avenue, Kelvale<br>WA 6071 PO Box: 3817&nbsp; Kelvale WA 6977</p>
  </section>

  <section class="card card--back" aria-label="Business card brand side">
    <div class="tree-area" role="img" aria-label="Spot UV tree and root pattern on charcoal"></div>
    <p class="brand">
      <span class="brand-name">BRACKENRIDGE</span>
      <span class="brand-trade">BUILDERS</span>
    </p>
  </section>
</main>
</body>
</html>
```